Attorney Website Design

I need a top quality attorney website layout designed. Here are some examples of what I feel are great websites:
http://www.quellmarstonseparationlaw.com/
http://www.vandriclegalgroup.com/
http://www.pobelaw.com/
http://www.harrowvaleaccusedcounselhq.com/
http://www.tzlegal.com/
http://www.brookhollowtrialjusticeoffice.com/
http://www.orvynchargedcounsel.com/
http://www.tzlegal.com/
What we like about these sites:
• The different layers
• Subtle designs, textures, curves
• 3 dimensional
• Floating effects
• Prominent phone number
• Location of Areas of Practice
• Request A Consultation Prominent
• Right side bar with practice areas
• Badges
• Clear Calls to Action
• Dynamic/Staying Top navigation when you scroll
The project will be for a home page and then also an interior page (should be similar to home page).
Updates
I want to make it understood I am looking for a design which is not a typical "template" site which I can find anywhere for $50. This budget and project is for a "Custom" website design. Please submit designs similar in quality to the samples links I have posted. Creativity is a MUST! The best way to explain this is, I want a design that I can feel it unique and original, not something that looks like 95% of all websites out there.
Neil
I just wanted everyone to know that so far I am not to pleased with any of the designs. I am not looking for cut/pasting of other peoples websites but ORIGINAL and CREATIVE work.
Reason: Weekend + Holiday extension.
Reason: Need more designs
Industry/Entity Type
Attorney

```html
<!DOCTYPE html>
<html lang="en">
<head>
<meta charset="utf-8">
<title>Harlow, Penwick, &amp; Dray — Family Law</title>
<link href="https://fonts.googleapis.com/css2?family=Crimson+Text:ital,wght@0,400;0,600;0,700;1,400&display=swap" rel="stylesheet">
<style>
  :root{
    --sky:#8e9fc6;
    --tan:#eebb82;
    --tan-light:#f1c696;
    --tan-field:#eab47a;
    --navy:#3c4e82;
    --navy-dark:#2f3f6d;
    --rust:#c9501c;
    --ink:#3b4a7e;
    --placeholder:#b9b9b9;
    --white:#ffffff;
  }
  *{box-sizing:border-box;margin:0;padding:0}
  html,body{width:1200px;height:1000px;overflow:hidden}
  body{background:var(--sky);font-family:"Crimson Text",Georgia,serif;color:var(--white);position:relative}
  .abs{position:absolute}

  .site-header{left:0;top:0;width:1200px;height:90px;background:var(--tan);box-shadow:0 2px 4px rgba(0,0,0,.35);z-index:5}
  .main-nav{right:216px;top:10px;display:flex;font-size:12px;color:var(--ink)}
  .main-nav a{color:var(--ink);text-decoration:none;margin-left:19px}
  .main-nav a.current{color:var(--rust);font-weight:700}
  .firm-intro{left:213px;top:31px;font-size:19px;color:var(--ink);line-height:1}
  .firm-name{left:213px;top:46px;font-size:34px;font-weight:700;color:var(--ink);line-height:1;letter-spacing:-.2px}
  .phone{right:216px;top:48px;text-align:right;color:var(--rust);line-height:1}
  .phone strong{display:block;font-size:20px;font-weight:700}
  .phone span{display:block;font-size:11px}

  .page{left:200px;top:90px;width:800px;height:910px}
  .hero{left:0;top:0;width:800px;height:266px;background:var(--placeholder);border:1px solid #9ea4b4}
  .hero-cta{left:13px;top:0;width:162px;height:28px;background:var(--tan-light);border-radius:0 0 4px 4px;box-shadow:0 2px 3px rgba(0,0,0,.3);font-size:11px;color:var(--rust);text-align:center;line-height:27px}
  .hero-kicker{left:472px;top:160px;font-style:italic;font-size:22px}
  .hero-title{left:500px;top:186px;font-size:47px;font-weight:700}

  .benefits{left:0;top:266px;width:800px;height:163px;background:var(--navy);box-shadow:inset 0 2px 3px rgba(0,0,0,.3)}
  .benefit-icon{width:105px;height:105px;background:var(--tan-light);border-radius:5px;box-shadow:0 2px 3px rgba(0,0,0,.35);top:25px}
  .benefit-icon svg{width:105px;height:105px}
  .benefit-title{font-size:19px;font-weight:700;color:var(--tan-light);line-height:20px;top:22px}
  .benefit-text{font-size:12px;line-height:13px;top:63px;width:132px}

  .consult{left:0;top:429px;width:800px;height:207px;background:var(--tan);border-top:2px solid var(--tan-light)}
  .consult h2{position:absolute;left:0;top:8px;width:800px;text-align:center;font-size:32px;font-weight:700;color:var(--ink)}
  .field{background:linear-gradient(var(--tan-field),var(--tan-field) 50%,var(--tan-light) 50%);border:2px solid var(--navy-dark);border-radius:4px;font-style:italic;font-size:16px;color:var(--ink);padding:6px 8px;box-shadow:0 1px 0 rgba(255,255,255,.5)}
  .terms{left:605px;top:92px;width:180px;font-size:11.5px;line-height:14px;color:var(--ink)}
  .terms a{color:var(--rust);text-decoration:none}
  .submit{left:605px;top:163px;width:180px;height:36px;background:linear-gradient(#4b5f96,var(--navy-dark));border-radius:4px;box-shadow:0 2px 3px rgba(0,0,0,.35);color:var(--white);font-size:25px;font-weight:700;text-align:center;line-height:34px}

  .lower{left:0;top:636px;width:800px;height:274px;background:var(--navy);box-shadow:inset 0 2px 3px rgba(0,0,0,.3);overflow:hidden}
  .col-rule{top:15px;width:2px;height:260px;background:var(--tan)}
  .section-title{font-size:19px;font-weight:700;color:var(--tan-light);line-height:1}
  .practice-sub{left:13px;top:33px;width:147px;text-align:center;font-style:italic;font-size:12px;color:var(--tan-light)}
  .practice-list{left:13px;top:61px;width:150px;list-style:none;font-size:13px;line-height:15px}
  .practice-list li{margin-bottom:4.3px;padding-left:9px;text-indent:-9px}
  .copy{font-size:12px;line-height:13.4px;width:378px}
  .video{left:589px;width:196px;height:125px;background:var(--placeholder);border:1px solid #8e8e8e}
  .video svg{width:100%;height:100%}
  .video-link{left:589px;top:169px;width:196px;text-align:center;font-size:13px;font-weight:700;color:var(--tan-light)}
</style>
</head>
<body>
  <header class="site-header abs">
    <nav class="main-nav abs">
      <a class="current" href="#">Home</a><a href="#">About</a><a href="#">Attorneys</a><a href="#">Areas of Practice</a><a href="#">Testimonials</a><a href="#">Free Consultation</a><a href="#" style="margin-left:24px">Contact</a>
    </nav>
    <div class="firm-intro abs">The Law Offices of</div>
    <div class="firm-name abs">Harlow, Penwick, &amp; Dray</div>
    <div class="phone abs"><strong>555.123.4567</strong><span>Hablamos Español</span></div>
  </header>

  <main class="page abs">
    <section class="hero abs" role="img" aria-label="Hero photograph of a family">
      <div class="hero-cta abs">Request a Free Consultation Now</div>
      <div class="hero-kicker abs">Unhappy Family?</div>
      <div class="hero-title abs">We Can Help</div>
    </section>

    <section class="benefits abs">
      <div class="benefit-icon abs" style="left:13px">
        <svg viewBox="0 0 105 105"><polygon fill="#3c4e82" points="52.5,14 62,42 92,42 68,60 77,90 52.5,72 28,90 37,60 13,42 43,42"/></svg>
      </div>
      <div class="benefit-title abs" style="left:127px">A Reputation<br>For Success</div>
      <div class="benefit-text abs" style="left:127px;top:63px">Since 19XX, we have provided families across the Gainesville area with unrivaled family litigation services.</div>

      <div class="benefit-icon abs" style="left:279px">
        <svg viewBox="0 0 105 105"><g fill="#3c4e82"><rect x="10" y="24" width="68" height="42" rx="2"/><rect x="18" y="32" width="72" height="46" rx="2" fill="#f1c696"/><rect x="20" y="34" width="68" height="42" rx="2"/><rect x="28" y="42" width="70" height="48" rx="2" fill="#f1c696"/><rect x="30" y="44" width="68" height="44" rx="2"/></g><text x="64" y="77" font-family="Georgia,serif" font-size="30" font-weight="700" fill="#f1c696" text-anchor="middle">$</text></svg>
      </div>
      <div class="benefit-title abs" style="left:392px">No Upfront Cost</div>
      <div class="benefit-text abs" style="left:392px;top:45px">We believe that money should be no cause for concern in legal affairs. Therefore, if we fail your case you do not have to pay us a single cent.</div>

      <div class="benefit-icon abs" style="left:541px">
        <svg viewBox="0 0 105 105"><g fill="#3c4e82" stroke="#3c4e82"><circle cx="52.5" cy="20" r="8"/><rect x="49" y="26" width="7" height="52" stroke="none"/><line x1="22" y1="40" x2="83" y2="40" stroke-width="4"/><path d="M12 64 L22 42 L32 64 Z" fill="none" stroke-width="2"/><path d="M10 64 Q22 76 34 64 Z"/><path d="M73 64 L83 42 L93 64 Z" fill="none" stroke-width="2"/><path d="M71 64 Q83 76 95 64 Z"/><path d="M30 92 Q52.5 68 75 92 Z"/></g></svg>
      </div>
      <div class="benefit-title abs" style="left:655px">Unparalleled<br>Legal Respect</div>
      <div class="benefit-text abs" style="left:655px">Our position in the courts and general legal community is one of the most storied and prestigious in the US.</div>
    </section>

    <section class="consult abs">
      <h2>Request a Free Consultation Now</h2>
      <div class="field abs" style="left:13px;top:49px;width:377px;height:36px">Name</div>
      <div class="field abs" style="left:406px;top:49px;width:181px;height:36px">Phone Number</div>
      <div class="field abs" style="left:605px;top:49px;width:180px;height:36px">Email</div>
      <div class="field abs" style="left:13px;top:96px;width:574px;height:102px">Describe your case here...</div>
      <div class="terms abs">By pressing the button below, you understand and agree to our <a href="#">Terms and Conditions</a> as set forth in the preceding link.</div>
      <div class="submit abs">Submit</div>
    </section>

    <section class="lower abs">
      <div class="section-title abs" style="left:13px;top:14px;width:147px;text-align:center">Areas of Practice</div>
      <div class="practice-sub abs">Family Law</div>
      <ul class="practice-list abs">
        <li>Divorce</li><li>Child Custody &amp; Visitation</li><li>Child &amp; Spousal Support</li><li>Prenuptial &amp; Postnuptial Agreement</li><li>Paternity Suits</li><li>Division of Marital Property</li><li>Domestic Partnerships</li><li>Same Sex Divorce</li><li>Post-Divorce Modifications</li><li>Guardianships</li>
      </ul>
      <div class="col-rule abs" style="left:173px"></div>

      <div class="section-title abs" style="left:190px;top:14px">Who We Are</div>
      <p class="copy abs" style="left:190px;top:39px">Phasellus malesuada sit amet justo sit amet egestas. Suspendisse potenti. Pellentesque feugiat dapibus est vitae pellentesque. Sed a justo pellentesque, aliquam velit rhoncus, pulvinar purus. Cras tristique massa est, at pulvinar mauris venenatis consequat. In quis dolor vulputate, placerat sem eget, sodales tellus. Etiam fermentum faucibus dignissim. Nam accumsan ut metus vel hendrerit. Vestibulum vitae pulvinar mauris, quis consequat ipsum.</p>
      <div class="section-title abs" style="left:190px;top:135px">Why Trust Us?</div>
      <p class="copy abs" style="left:190px;top:160px">Pellentesque sit amet eleifend purus. Cum sociis natoque penatibus et magnis dis parturient montes, nascetur ridiculus mus. Integer sed tortor vel nunc scelerisque cursus. Mauris a rhoncus dui. Praesent consectetur pellentesque tellus nec ornare. Cras bibendum, nisl ac ullamcorper viverra, ipsum felis pharetra justo, sit amet auctor sapien nunc vel lectus. Cras et mollis nisl. Nulla facilisi. Curabitur eget eleifend risus, tincidunt scelerisque diam. Interdum et malesuada fames ac ante ipsum primis in faucibus. Maecenas massa dui, lacinia a facilisis non, posuere vitae neque. Phasellus dictum suscipit, ut convallis lacus.</p>
      <div class="col-rule abs" style="left:578px"></div>

      <div class="section-title abs" style="left:589px;top:14px">Video Center</div>
      <div class="video abs" style="top:39px" role="img" aria-label="Firm introduction video">
        <svg viewBox="0 0 196 125"><circle cx="98" cy="61" r="33" fill="#dedede"/><polygon points="88,44 88,78 118,61" fill="#777"/></svg>
      </div>
      <div class="video-link abs">Learn More About Our Firm</div>
      <div class="video abs" style="top:218px" role="img" aria-label="Client testimonial video">
        <svg viewBox="0 0 196 125"><circle cx="98" cy="61" r="33" fill="#dedede"/><polygon points="88,44 88,78 118,61" fill="#777"/></svg>
      </div>
    </section>
  </main>
</body>
</html>
```